Brightpath Wellness Partners

Please design a business card that is colorful but at the same time easy to read. We are based out on Miami Florida. We are a small start up healthcare company that has been in operation for 1 year. Our clients are Hospitals, Insurance companies, and Manage Care health companies. We are growing quickly and lead the niche we are in. Please make the card 2 sided on the front will be the typical info. Logo, Company Name, Persons Name, Title, Cell #, Office #, Fax#, email, website. No address. On the back we will list 5 services that we do. For example Care Transitions, Case management, Risk assessment, Utilization Review.
Target Market(s)
CEO's and COO's of hospitals and healthcare companies.
Industry/Entity Type
Healthcare

```html
<!DOCTYPE html>
<html lang="en">
<head>
<meta charset="utf-8">
<title>Brightpath Wellness Partners – Business Cards</title>
<link rel="stylesheet" href="https://fonts.googleapis.com/css2?family=Oswald:wght@500&family=Roboto:wght@400;700&display=swap">
<style>
  :root {
    --backdrop: #d9d9d9;
    --card: #ffffff;
    --brand-navy: #1f2a7a;
    --name-blue: #3b63d8;
    --ink: #555a60;
    --rule: #c9cbcf;
    --icon-tile: #2b3138;
    --accent-blue: #2f6fd6;
    --accent-green: #3fae49;
    --accent-yellow: #f2c21b;
    --accent-red: #e23b3b;
    --accent-sky: #3fa4e0;
  }
  * { box-sizing: border-box; margin: 0; padding: 0; }
  html, body { width: 1200px; height: 988px; overflow: hidden; }
  body {
    background: var(--backdrop);
    font-family: "Roboto", Arial, sans-serif;
    display: flex; flex-direction: column; align-items: center; justify-content: center;
    gap: 40px;
  }
  .card {
    width: 760px; height: 434px;
    background: var(--card);
    box-shadow: 0 6px 18px rgba(0,0,0,.18);
    position: relative;
    overflow: hidden;
  }
  .color-stripe {
    position: absolute; left: 0; right: 0; bottom: 0; height: 6px;
    background: linear-gradient(90deg,
      var(--accent-blue) 0 25%, var(--accent-green) 25% 50%,
      var(--accent-yellow) 50% 75%, var(--accent-red) 75% 100%);
  }
  .brand {
    display: flex; align-items: center; gap: 16px;
    color: var(--brand-navy);
    font-weight: 700;
  }
  .brand-dot {
    width: 52px; height: 52px; border-radius: 50%;
    background: var(--brand-navy);
    flex: none;
  }
  .brand-name { font-size: 24px; line-height: 1.15; }

  /* Services side */
  .card-services .brand { position: absolute; left: 50%; top: 64px; transform: translateX(-50%); }
  .services-heading {
    position: absolute; left: 0; right: 0; top: 200px;
    text-align: center;
    font-family: "Oswald", "Arial Narrow", sans-serif;
    font-weight: 500; font-size: 15px; letter-spacing: 3px;
    color: var(--name-blue); text-transform: uppercase;
  }
  .service-list {
    position: absolute; left: 110px; right: 110px; top: 240px;
    list-style: none;
    display: grid; grid-template-columns: 1fr 1fr; column-gap: 50px; row-gap: 14px;
  }
  .service-list li {
    display: flex; align-items: center; gap: 12px;
    font-size: 15px; color: var(--ink);
    padding-bottom: 10px; border-bottom: 1px solid var(--rule);
  }
  .service-dot { width: 12px; height: 12px; border-radius: 50%; flex: none; }
  .dot-blue { background: var(--accent-blue); }
  .dot-green { background: var(--accent-green); }
  .dot-yellow { background: var(--accent-yellow); }
  .dot-red { background: var(--accent-red); }
  .dot-sky { background: var(--accent-sky); }

  /* Contact side */
  .card-contact .brand { position: absolute; left: 50%; top: 46px; transform: translateX(-50%); }
  .card-contact .brand-dot { width: 46px; height: 46px; }
  .card-contact .brand-name { font-size: 21px; }
  .divider {
    position: absolute; left: 390px; right: 50px; top: 168px;
    border-top: 1px solid var(--rule);
  }
  .person { position: absolute; left: 50px; top: 196px; width: 300px; }
  .person-name {
    font-family: "Oswald", "Arial Narrow", sans-serif;
    font-weight: 500; font-size: 30px; letter-spacing: 1px;
    color: var(--name-blue); text-transform: uppercase; line-height: 1.1;
  }
  .person-title { font-size: 12px; letter-spacing: 2px; color: var(--ink); text-transform: uppercase; margin-top: 4px; }
  .contact-list { list-style: none; margin-top: 12px; }
  .contact-list li {
    display: flex; align-items: center; gap: 14px;
    font-size: 14px; color: var(--ink);
    padding: 7px 0; border-bottom: 1px solid var(--rule);
  }
  .contact-label { width: 46px; font-size: 11px; letter-spacing: 1px; text-transform: uppercase; color: #8a8f95; }
  .contact-web { position: absolute; left: 400px; top: 200px; width: 310px; }
  .icon {
    width: 28px; height: 28px; border-radius: 5px;
    background: var(--icon-tile);
    display: flex; align-items: center; justify-content: center; flex: none;
  }
  .icon svg { width: 16px; height: 16px; fill: none; stroke-width: 2; stroke-linecap: round; stroke-linejoin: round; }
  .glyph-blue { stroke: var(--accent-sky); }
  .glyph-green { stroke: var(--accent-green); }
  .glyph-yellow { stroke: var(--accent-yellow); }
  .glyph-red { stroke: var(--accent-red); }
</style>
</head>
<body>
  <section class="card card-services" aria-label="Card back – services">
    <div class="brand">
      <span class="brand-dot"></span>
      <span class="brand-name">Brightpath<br>Wellness<br>Partners</span>
    </div>
    <h2 class="services-heading">Our Services</h2>
    <ul class="service-list">
      <li><span class="service-dot dot-blue"></span>Care Transitions</li>
      <li><span class="service-dot dot-green"></span>Case Management</li>
      <li><span class="service-dot dot-yellow"></span>Risk Assessment</li>
      <li><span class="service-dot dot-red"></span>Utilization Review</li>
      <li><span class="service-dot dot-sky"></span>Discharge Planning</li>
    </ul>
    <div class="color-stripe"></div>
  </section>

  <section class="card card-contact" aria-label="Card front – contact">
    <div class="brand">
      <span class="brand-dot"></span>
      <span class="brand-name">Brightpath<br>Wellness<br>Partners</span>
    </div>
    <div class="divider"></div>

    <div class="person">
      <h1 class="person-name">Daniel Rivera</h1>
      <p class="person-title">Financial Advisor</p>
      <ul class="contact-list">
        <li><span class="icon"><svg class="glyph-green" viewBox="0 0 24 24"><rect x="6" y="2" width="12" height="20" rx="2"/><path d="M11 18h2"/></svg></span><span class="contact-label">Cell</span>305 555 0142</li>
        <li><span class="icon"><svg class="glyph-blue" viewBox="0 0 24 24"><path d="M5 3h4l2 5-3 2a12 12 0 0 0 6 6l2-3 5 2v4a2 2 0 0 1-2 2A17 17 0 0 1 3 5a2 2 0 0 1 2-2z"/></svg></span><span class="contact-label">Office</span>305 555 0187</li>
        <li><span class="icon"><svg class="glyph-red" viewBox="0 0 24 24"><path d="M7 8V3h10v5"/><rect x="3" y="8" width="18" height="9" rx="2"/><rect x="7" y="14" width="10" height="7"/></svg></span><span class="contact-label">Fax</span>305 555 0199</li>
      </ul>
    </div>

    <ul class="contact-list contact-web">
      <li><span class="icon"><svg class="glyph-yellow" viewBox="0 0 24 24"><rect x="3" y="5" width="18" height="14" rx="2"/><path d="M3 7l9 6 9-6"/></svg></span>hello@brightpathwp.com</li>
      <li><span class="icon"><svg class="glyph-blue" viewBox="0 0 24 24"><circle cx="12" cy="12" r="9"/><path d="M3 12h18M12 3a14 14 0 0 1 0 18M12 3a14 14 0 0 0 0 18"/></svg></span>www.brightpathwp.com</li>
    </ul>
    <div class="color-stripe"></div>
  </section>
</body>
</html>
```